Velmorytrips.com web design project + logo design

Hi,

We are a Russian online tour operator - roamquiltex.com

We are looking to tranmsfer our domain to velmorytrips.com. The website and logo need to be velmoryesque - we are not looking to change our functionality, but we need to make the website much more attracitve to clients, much more wild looking but at the same time remaining a professional travel company.

The main concept of the website should be innovative travel (as velmory was an innovator). Alternatively, you could go down the artist route and go down the draw / design your own tour road.

On our website the customer is able to combine travel services (hotels, flights, Visa services, and soon chauffeur, car rental etc...) put it into their basket (the basket definitely has to look better than it is at the moment) and pay for it in one go by card.

We are also stressin our customer support with web chat, call centre etc... (call centre number at the top of the page)

We aim to provide an easy user experience, but we need to make it have some more style, so I will be waiting for what you guys can come up with.
Let me know if you have any questions - skype is: mrkostelin

Industry/Entity Type

It Company

Logo Text

Requirements
Must have
• It is quite a simple task - to take the existing website roamquiltex.com and velmorysize it to create velmorytrips.com, the functionality of the website will remain the same and there are not many pages in the website. Homepage, Checkout step1, Checkout step 2 (you can view both of these if you select a service) and the generic pages for T&C''s, Privacy policy etc...

IMPORTANT UPDATE

We are also looking at how the search results will look in the designs, (please do a search on our website for hotel / flight)

```html
<!DOCTYPE html>
<html lang="en">
<head>
<meta charset="utf-8">
<title>Velmory Travel</title>
<link href="https://fonts.googleapis.com/css2?family=Questrial&display=swap" rel="stylesheet">
<style>
:root{
  --ink:#2e2e2e;
  --top:#262626;
  --head:#333333;
  --accent:#f5c21b;
  --white:#ffffff;
  --muted:#6a6a6a;
  --red:#e4495a;
  --cyan:#2cc4df;
  --yellow:#f5c400;
  --info:#e3c400;
  --purple:#7530ae;
  --green:#1eae58;
  --paper:#f1f1f1;
  --foot:#e3e3e3;
}
*{box-sizing:border-box;margin:0;padding:0}
html,body{width:797px;height:1200px;overflow:hidden}
body{position:relative;font-family:"Questrial",sans-serif;color:var(--ink);background:var(--paper)}
.abs{position:absolute}
.topbar{left:0;top:0;width:797px;height:33px;background:var(--top)}
.phone{left:429px;top:9px;font-size:14px;color:var(--accent);display:flex;align-items:center;gap:6px}
.toplinks{left:562px;top:12px;font-size:8px;color:#ddd;display:flex;gap:6px;align-items:center}
.flag{width:12px;height:8px;background:linear-gradient(#fff 33%,#2848b8 33% 66%,#d62b2b 66%)}
.header{left:0;top:33px;width:797px;height:106px;background:var(--head)}
.logo{left:86px;top:59px;display:flex;align-items:center;gap:8px}
.logo-dot{width:26px;height:26px;border-radius:50%;background:var(--accent)}
.logo-name{font-size:29px;color:var(--accent);letter-spacing:.5px}
.search{left:544px;top:63px;width:164px;height:17px;background:#fff;border:1px solid #ccc;font-size:6px;color:#aaa;padding:4px 6px}
.search svg{position:absolute;right:4px;top:3px}
.nav{left:86px;top:108px;display:flex;gap:13px;font-size:13px;color:#eee}
.nav .on{color:var(--accent)}
.basket{left:511px;top:94px;width:199px;height:34px;background:linear-gradient(#fafafa,#dcdcdc);display:flex;font-size:8.5px;color:#333}
.basket div{display:flex;align-items:center;justify-content:center;border-right:1px solid #c6c6c6}
.basket .b1{width:59px;font-size:9px;gap:3px}
.basket .b1 span{width:14px;height:16px;background:#7cc04a;border-radius:2px}
.basket .b2{width:42px}.basket .b3{width:50px}.basket .b4{width:48px;border:0}
.hero{left:0;top:139px;width:797px;height:342px;background:linear-gradient(180deg,#3a62b8 0%,#6b8fd0 22%,#e8a45a 55%,#f07a2a 75%,#8a4a2a 100%)}
.dots{left:81px;top:408px;display:flex;gap:3px}
.dots i{width:9px;height:9px;border-radius:50%;background:#222;border:1.5px solid #fff}
.dots i:first-child{background:#fff;border-color:#222}
.tabs{left:511px;top:183px;width:199px;height:25px}
.tab{position:absolute;color:#fff;font-size:12px;padding-left:12px;line-height:22px}
.t1{left:0;top:0;width:64px;height:25px;background:var(--red)}
.t2{left:67px;top:6px;width:65px;height:19px;background:var(--cyan);line-height:19px}
.t3{left:135px;top:6px;width:64px;height:19px;background:var(--yellow);line-height:19px}
.panel{left:511px;top:208px;width:199px;height:208px;background:rgba(240,118,66,.72);font-size:7.5px;color:#f4d8c8}
.field{position:absolute;background:#fff;border:1px solid #ddd;border-radius:2px;color:#aaa;font-size:7.5px;padding:5px 4px}
.field b{position:absolute;right:6px;top:4px;color:#333;font-weight:normal;font-size:7px}
.radio{position:absolute;width:8px;height:8px;border-radius:50%;background:#fff}
.btn{left:56px;top:181px;width:91px;height:20px;background:#222;color:#fff;font-size:9px;text-align:center;line-height:20px;border-radius:2px;position:absolute}
.features{left:80px;top:449px;width:637px;height:260px;background:#fff}
.h2{font-size:15px;color:#333}
.ftitle{left:0;width:637px;top:14px;text-align:center}
.card{position:absolute;top:44px;width:199px;height:199px;color:#fff;padding:18px 12px;font-size:7.5px;line-height:12px}
.card h3{font-weight:normal;font-size:12.5px;display:flex;align-items:center;gap:8px;margin-bottom:12px}
.card .lead{font-size:9px;line-height:12px;margin-bottom:8px}
.c1{left:6px;background:var(--info)}.c2{left:218px;background:var(--purple)}.c3{left:431px;background:var(--green)}
.c1 .lead{margin-bottom:10px}
.photo{position:absolute}
.welcome-img{left:86px;top:752px;width:199px;height:132px;background:linear-gradient(180deg,#4da4e2,#a8d8f2 55%,#2f78b8)}
.welcome-text{left:298px;top:749px;width:200px;font-size:7.6px;line-height:13.3px;color:#555;text-align:justify}
.more{left:451px;top:875px;font-size:8px;color:#333}
.gallery-img{left:511px;top:752px;width:199px;height:132px;background:linear-gradient(180deg,#5f8ed4,#b9cde8 60%,#3e6fb0)}
.arrows{left:689px;top:724px;font-size:12px;color:#444;letter-spacing:6px}
.testi{left:0;top:914px;width:797px;text-align:center}
.testi p{font-size:10.4px;line-height:15px;color:#444;margin:12px auto 0;width:620px}
.testi .name{font-size:10.5px;color:#222;margin-top:1px}
.footer{left:0;top:1019px;width:797px;height:181px;background:var(--foot)}
.fh{position:absolute;top:31px;font-size:11.5px;color:#333}
.fl{position:absolute;top:67px;font-size:7.5px;color:#555;line-height:16px}
.fl div{display:flex;align-items:center;gap:6px}
.fl i{width:9px;height:9px;background:#444;display:inline-block}
.soc{position:absolute;top:66px;text-align:center;font-size:7.5px;color:#444;width:60px}
.soc span{display:block;width:19px;height:19px;border-radius:50%;background:#555;margin:0 auto 8px}
.soc .sq{border-radius:2px;background:none;border:1.5px solid #555;width:15px;height:15px}
.copy{left:0;top:1150px;width:797px;text-align:center;font-size:9px;color:#444}
</style>
</head>
<body>
<div class="abs topbar"></div>
<div class="abs phone"><svg width="10" height="12" viewBox="0 0 10 12"><path d="M2 0l2 3-1 1c0 2 2 4 3 4l1-1 3 2-2 3C4 11-1 6 0 2z" fill="#777"/></svg>8-800-555-0142</div>
<div class="abs toplinks"><span>Forum |</span><span>My Tour |</span><span>Language</span><span class="flag"></span><span>▾</span></div>

<header class="abs header"></header>
<div class="abs logo"><span class="logo-dot"></span><span class="logo-name">Velmory Travel</span></div>
<div class="abs search">Type search<svg width="9" height="9" viewBox="0 0 9 9"><circle cx="3.5" cy="3.5" r="2.7" fill="none" stroke="#999"/><path d="M5.5 5.5L8.5 8.5" stroke="#999"/></svg></div>
<nav class="abs nav"><span class="on">Home</span><span>About Us</span><span>Travel</span><span>Special Offers</span><span>Book Your Tour</span><span>Contact Us</span></nav>
<div class="abs basket"><div class="b1">BASKET<span></span></div><div class="b2">Empty</div><div class="b3">Payment</div><div class="b4">Pricing</div></div>

<div class="abs hero" role="img" aria-label="Eiffel Tower against a sunset sky over Paris rooftops"></div>
<div class="abs dots"><i></i><i></i><i></i><i></i></div>

<div class="abs tabs"><div class="tab t1">Travel</div><div class="tab t2">Info</div><div class="tab t3">Ticket</div></div>
<form class="abs panel">
  <div class="field" style="left:10px;top:17px;width:179px;height:20px">When<b>▼</b></div>
  <div class="field" style="left:10px;top:50px;width:179px;height:20px">Where<b>▼</b></div>
  <div class="field" style="left:10px;top:82px;width:85px;height:20px">There<b>▦</b></div>
  <div class="field" style="left:103px;top:82px;width:86px;height:20px">Back<b>▦</b></div>
  <span class="radio" style="left:14px;top:110px"></span><span class="radio" style="left:97px;top:110px"></span>
  <span class="abs" style="left:13px;top:134px">Passenger</span>
  <div class="field" style="left:64px;top:130px;width:36px;height:16px;padding:3px 4px;font-size:6.5px">Men<b style="top:2px">▼</b></div>
  <div class="field" style="left:107px;top:130px;width:36px;height:16px;padding:3px 2px;font-size:6.5px">Women<b style="top:2px;right:1px">▼</b></div>
  <div class="field" style="left:152px;top:130px;width:36px;height:16px;padding:3px 2px;font-size:6.5px">Babies<b style="top:2px;right:1px">▼</b></div>
  <span class="abs" style="left:13px;top:158px">Class</span>
  <div class="field" style="left:64px;top:153px;width:85px;height:20px">Economy<b>▼</b></div>
  <div class="btn">SEARCH</div>
</form>

<section class="abs features">
  <div class="abs h2 ftitle">Our Features</div>
  <div class="card c1"><h3><svg width="13" height="16" viewBox="0 0 13 16"><path d="M1 1h8l3 3v11H1z" fill="none" stroke="#fff"/><path d="M3 7h7M3 10h7M3 13h5" stroke="#fff"/></svg>Info</h3>
    <p class="lead">There are two options apply for a visa</p>
    <p class="lead" style="margin-bottom:6px">1.Oformlenie visa "Online"</p>
    <p class="lead" style="margin-bottom:14px">2. Visa "Myself."</p>
    <p>Lorem Ipsum is simply dummy text of the printing and typesetting industry. Lorem Ipsum has been the industry's standard dummy text ever since the 1500s,</p></div>
  <div class="card c2"><h3><svg width="26" height="12" viewBox="0 0 26 12"><rect x="1" y="1" width="24" height="10" rx="2" fill="none" stroke="#fff"/><rect x="4" y="3.5" width="18" height="5" fill="none" stroke="#fff" stroke-width=".6"/></svg>Tickets</h3>
    <p class="lead">Flights from Tours designer.</p>
    <p>On our site you can consider offers from different airlines and purchase tickets according to your wishes and budget. Plan dates of departures and arrivals c in any country, filling the cells you want, Tour Designer automatically displays your program in the calendar. On Tour Designer You can create any tour, including round-the-world and pay for all the services a single payment.</p></div>
  <div class="card c3"><h3><svg width="14" height="16" viewBox="0 0 14 16"><path d="M7 1c3 0 4 3 4 6v3l2 2H1l2-2V7c0-3 1-6 4-6z" fill="#fff"/><circle cx="7" cy="14" r="1.6" fill="#fff"/></svg>Hotels</h3>
    <p class="lead">Hotels by City Builder.</p>
    <p>Our site offers a wide selection of hotels located in different countries and continents of the world. You can choose and book all kinds of accommodation options, according to your wishes and budget. pursue their dreams! We have created for you the most convenient framework for planning a vacation or business trip.</p></div>
</section>

<div class="abs h2" style="left:82px;top:724px;font-size:13px">Welcomet to Velmory Travel</div>
<div class="photo welcome-img" role="img" aria-label="Globe with world landmarks and airplanes flying around it"></div>
<p class="abs welcome-text">Lorem Ipsum is simply dummy text of the printing and typesetting industry. Lorem Ipsum has been the industry's standard dummy text ever since the 1500s, when an unknown printer took a galley of type and scrambled it to make a type specimen book. It has survived not only five centuries, but also the leap into electronic typesetting, remaining essentially unchanged. Lorem Ipsum is simply dummy text of the printing and typesetting industry.</p>
<div class="abs more">Read More</div>
<div class="abs h2" style="left:511px;top:724px;font-size:13px">Photo Gallery</div>
<div class="abs arrows">‹ ›</div>
<div class="photo gallery-img" role="img" aria-label="Sail-shaped seaside hotel tower with resort thumbnails below"></div>

<section class="abs testi">
  <div class="h2" style="font-size:12.5px">Testimonials</div>
  <p>Lorem ipsum dolor sit amet, consectetur adipisicing elit, sed do eiusmod tempor incididunt ut labore et dolore magna aliqua. Ut enim ad minim veniam, quis nostrud exercitation ullamco laboris nisi ut aliquip ex ea commodo consequat.</p>
  <p style="margin-top:0">By</p>
  <div class="name">Edmund Parrow</div>
</section>

<footer class="abs footer">
  <div class="fh" style="left:86px">View Site</div>
  <div class="fh" style="left:192px">Help</div>
  <div class="fh" style="left:299px">Find Us</div>
  <div class="fh" style="left:406px">Contact</div>
  <div class="fh" style="left:567px">Connect With Us</div>
  <div class="fl" style="left:86px">Home<br>About Us<br>Forum<br>Contacts</div>
  <div class="fl" style="left:192px">Help<br>Terms of use<br>Privacy Policy<br>Cookies</div>
  <div class="fl" style="left:299px">Roamquiltex Limited<br>14 Harrow Lane<br>Brenfield, BF2 7QX ,UK</div>
  <div class="fl" style="left:413px"><div><i></i>+7 (495) 555-01-27</div><div><i></i>info@Velmorytrips.com</div><div><i></i>Эксклюзивные предложения</div></div>
  <div class="soc" style="left:559px"><span></span>Chirpline</div>
  <div class="soc" style="left:609px"><span></span>Pagebook</div>
  <div class="soc" style="left:659px"><span class="sq"></span>Social Icon</div>
</footer>
<div class="abs copy">©2013 Velmory Travel &nbsp;|&nbsp; All Rights Reserved</div>
</body>
</html>
```